International Dating Community Needs a Web Design

We need a single page web design built on plenvo.com. Designers need to design a one page web design on PLENVO, take a screenshot and paste it here. Once the winner is chosen, the designer needs to give me access to the design and transfer over the implementation.
REQUIREMENTS:
- Designer MUST design on plenvo.com (http://www.plenvo.com/support/main/html5/getting-started/signing-free)
- Once designed, designer needs to take a screenshot of the plenvo design and submit the design on artquarry.
- Please add the site url as the design comment when you submit the design
- Any designers that use existing PLENVO templates will NOT be eligible to win and will be eliminated.
Note: If you use any stock images, simply let me know the numbers and I will purchase them.
PAGE INFORMATION:
Color Scheme:
- Light Blue / Cyan
- White
- Black / Dark Gray
Header:
- Logo (attached) on the left
- Login / Register on the right
Navigation bar:
- Home
- Events
- Entertainment / Music
- Gallery
- Membership
- About Us
Homepage Content:
The worlds #1 destination for international dating!
We may be new to you, but our team have been around for longer than you think. We're here to promote upcoming cultural events in your community, promote local businesses serving your community & soon we will also be offering an online dating service to meet others within the area.
If you're interested in learning more about events & concerts relating to the community then make sure you like us on Chatterloom.
If you have any comments or feedback, we'd love to hear from you! Click here to contact us.
Photos:
Im open for you to use any photos you like - some sites I like:
http://www.brightstockpix.net/images/People_g40.html
http://www.qvt.hu/category/135
Entertainment

```html
<!DOCTYPE html>
<html lang="en">
<head>
<meta charset="utf-8">
<title>Amiora – International Dating Community</title>
<link rel="stylesheet" href="https://fonts.googleapis.com/css2?family=Open+Sans:wght@300;400;600;700&display=swap">
<style>
  :root {
    --cyan: #40e1d1;
    --cyan-deep: #2fcfbf;
    --white: #ffffff;
    --ink: #1e1e1e;
    --photo-yellow: #d9b63c;
    --photo-magenta: #8a2a7a;
    --photo-purple: #4a2a8a;
    --photo-blue: #2b3fa0;
  }
  * { box-sizing: border-box; margin: 0; padding: 0; }
  html, body { width: 1200px; height: 1000px; overflow: hidden; background: var(--ink); }
  body { font-family: "Open Sans", Arial, sans-serif; color: var(--white); }

  .page { position: relative; width: 1200px; height: 1000px; }

  .hero { position: relative; height: 600px; overflow: hidden; }
  .hero-photo {
    position: absolute; inset: 0;
    background:
      radial-gradient(ellipse at 30% 60%, rgba(60,90,160,0.55), transparent 45%),
      radial-gradient(ellipse at 70% 55%, rgba(40,60,170,0.6), transparent 45%),
      linear-gradient(90deg, var(--photo-yellow) 0%, #c49a48 22%, var(--photo-magenta) 55%, var(--photo-purple) 80%, #3a2470 100%);
  }

  .site-header {
    position: absolute; top: 22px; left: 0; right: 0;
    display: flex; align-items: center; justify-content: center; gap: 28px;
  }
  .brand {
    background: var(--cyan); padding: 6px 14px;
    font-size: 26px; font-weight: 400; color: var(--white); letter-spacing: 0.5px;
  }
  .main-nav { display: flex; gap: 6px; font-size: 14px; font-weight: 600; text-transform: uppercase; }
  .main-nav a { color: var(--white); text-decoration: none; }
  .main-nav span { opacity: 0.9; }

  .headline-arc { position: absolute; left: 340px; top: 90px; width: 520px; height: 170px; }
  .heart { position: absolute; left: 517px; top: 215px; width: 166px; height: 146px; }
  .tagline {
    position: absolute; top: 395px; left: 0; right: 0; text-align: center;
    font-size: 29px; font-weight: 700; letter-spacing: 0.3px;
  }
  .scroll-down {
    position: absolute; top: 480px; left: 0; right: 0;
    display: flex; flex-direction: column; align-items: center; gap: 6px;
    font-size: 14px; text-transform: uppercase;
  }

  .intro {
    height: 400px; background: var(--cyan);
    display: flex; flex-direction: column; align-items: center;
    padding-top: 48px; text-align: center;
  }
  .intro-lead { font-size: 25px; font-weight: 700; line-height: 1.35; text-transform: uppercase; }
  .intro-brand { margin-top: 44px; font-size: 64px; font-weight: 300; line-height: 1; }
  .intro-sub { margin-top: 8px; font-size: 21px; font-weight: 300; }
  .intro-mission { margin-top: 52px; font-size: 18px; font-weight: 700; text-transform: uppercase; letter-spacing: 0.5px; }
</style>
</head>
<body>
<main class="page">
  <section class="hero">
    <div class="hero-photo" role="img" aria-label="Photo of two young women in sunglasses posing against a brick wall, washed in yellow, magenta and blue light"></div>

    <header class="site-header">
      <div class="brand">amiora</div>
      <nav class="main-nav">
        <a href="#">Home</a><span>-</span>
        <a href="#">Events</a><span>-</span>
        <a href="#">Entertainment / Music</a><span>-</span>
        <a href="#">Gallery</a><span>-</span>
        <a href="#">Membership</a><span>-</span>
        <a href="#">About Us</a>
      </nav>
    </header>

    <svg class="headline-arc" viewBox="0 0 520 170" aria-label="The Worlds #1">
      <defs><path id="arc" d="M40 165 Q260 -30 480 165"/></defs>
      <text font-family="Open Sans, Arial, sans-serif" font-size="48" font-weight="700" fill="#ffffff">
        <textPath href="#arc" startOffset="50%" text-anchor="middle">THE <tspan fill="#40e1d1" font-weight="400">WORLDS</tspan> #1</textPath>
      </text>
    </svg>

    <svg class="heart" viewBox="0 0 166 146" aria-hidden="true">
      <path d="M83 146 L14 76 C-6 55 -4 22 18 8 C40 -6 68 2 83 24 C98 2 126 -6 148 8 C170 22 172 55 152 76 Z" fill="#ffffff"/>
    </svg>

    <p class="tagline">DESTINATION FOR INTERNATIONAL DATING!</p>

    <div class="scroll-down">
      <svg width="26" height="26" viewBox="0 0 26 26" aria-hidden="true">
        <circle cx="13" cy="13" r="11.5" fill="none" stroke="#fff" stroke-width="2"/>
        <path d="M8 11 L13 16 L18 11" fill="none" stroke="#fff" stroke-width="2"/>
      </svg>
      <span>Scroll down</span>
    </div>
  </section>

  <section class="intro">
    <p class="intro-lead">We may be new to you, but our team have been<br>around for longer than you think.</p>
    <p class="intro-brand">amiora</p>
    <p class="intro-sub">international dating community</p>
    <p class="intro-mission">We're here to</p>
  </section>
</main>
</body>
</html>
```